Training Certificate Design

Project: I will like to design a training certificate for our company with details below;

Company Logo

This is to Certify that
"Name of student"
Has completed the
TRDX Linking and Bridging v5.2 training
His practical work has been evaluated and demonstrated knowledge and experience.
on "Date"

Registration Number
58719026.4170952

Certificate Number
WPMR6830215574

Signature space
Adewunmi .T. Marcellus
Chief Executive Officer

NOTE:

Find attached out company logo, our partner company logo, sample certificate and my signature.

```html
<!DOCTYPE html>
<html lang="en">
<head>
<meta charset="utf-8">
<title>Training Certificate</title>
<link rel="stylesheet" href="https://fonts.googleapis.com/css2?family=Dancing+Script:wght@700&family=Great+Vibes&family=Rajdhani:wght@500&family=Montserrat:wght@500&family=Arvo:wght@700&display=swap">
<style>
  :root {
    --ink: #111111;
    --blue-deep: #1565b8;
    --blue-light: #5cc6f0;
    --gray-dark: #1e1e1e;
    --gray-mid: #9a9a9a;
    --badge: #e6eef6;
    --paper: #ffffff;
  }
  html, body { margin: 0; padding: 0; overflow: hidden; background: var(--paper); }
  .certificate {
    position: relative;
    width: 848px;
    height: 1200px;
    background: var(--paper);
    overflow: hidden;
    color: var(--ink);
  }
  .swooshes { position: absolute; inset: 0; }
  .abs { position: absolute; left: 0; width: 100%; text-align: center; margin: 0; }

  .brand-mark {
    position: absolute; left: 383px; top: 84px;
    width: 90px; height: 90px; border-radius: 50%;
    background: var(--ink);
  }
  .brand-name {
    position: absolute; left: 278px; top: 182px; width: 300px; margin: 0;
    text-align: center;
    font-family: "Montserrat", sans-serif; font-weight: 500;
    font-size: 12px; line-height: 16px; color: var(--ink);
  }
  .partner-badge {
    position: absolute; left: 700px; top: 130px;
    width: 140px; height: 108px; background: var(--badge);
  }

  .script-heading {
    font-family: "Dancing Script", cursive; font-weight: 700;
    font-size: 44px; line-height: 1;
  }
  .certify { top: 238px; }
  .completed { top: 390px; }

  .recipient {
    position: absolute; left: 231px; top: 300px; width: 391px; height: 48px;
    border-bottom: 4px dotted var(--ink);
    font-family: "Great Vibes", cursive; font-size: 38px; line-height: 52px;
    text-align: center;
  }
  .course {
    top: 458px;
    font-family: "Rajdhani", sans-serif; font-weight: 500;
    font-size: 44px; line-height: 52px; letter-spacing: 1px;
  }
  .statement {
    top: 582px;
    font-family: "Montserrat", sans-serif; font-weight: 500;
    font-size: 24px; line-height: 29px;
  }
  .date {
    position: absolute; left: 350px; top: 656px; margin: 0;
    font-family: "Rajdhani", sans-serif; font-weight: 500; font-size: 28px;
  }
  .field { position: absolute; left: 259px; width: 316px; text-align: center; }
  .field-value {
    font-family: "Rajdhani", sans-serif; font-weight: 500; font-size: 31px;
    line-height: 32px; padding-bottom: 2px;
    border-bottom: 2px dotted var(--ink);
  }
  .field-label {
    font-family: "Rajdhani", sans-serif; font-weight: 500; font-size: 29px;
    letter-spacing: 1px; margin-top: 4px;
  }
  .registration { top: 709px; }
  .certificate-no { top: 806px; }

  .signatory { position: absolute; left: 259px; top: 902px; width: 316px; text-align: center; }
  .signature {
    display: block; margin: 0 auto; width: 226px; height: 82px;
    background: linear-gradient(90deg, #e9e9e9, #d4d4d4);
    border-bottom: 2px dotted var(--ink);
  }
  .signatory-name {
    font-family: "Rajdhani", sans-serif; font-weight: 500; font-size: 29px;
    letter-spacing: 1px; margin-top: 8px; line-height: 34px;
  }
  .signatory-role {
    font-family: "Arvo", serif; font-weight: 700; font-size: 28px;
    line-height: 35px; letter-spacing: 1px;
  }
</style>
</head>
<body>
<main class="certificate">
  <svg class="swooshes" viewBox="0 0 848 1200" width="848" height="1200" aria-hidden="true">
    <defs>
      <linearGradient id="blueBand" x1="0" y1="0" x2="1" y2="0">
        <stop offset="0" stop-color="var(--blue-deep)"/>
        <stop offset="1" stop-color="var(--blue-light)"/>
      </linearGradient>
      <linearGradient id="grayBandTop" x1="0" y1="0" x2="1" y2="0">
        <stop offset="0" stop-color="var(--gray-dark)"/>
        <stop offset="0.45" stop-color="var(--gray-mid)"/>
        <stop offset="1" stop-color="#ffffff"/>
      </linearGradient>
      <linearGradient id="grayBandBottom" gradientUnits="userSpaceOnUse" x1="848" y1="0" x2="520" y2="0">
        <stop offset="0" stop-color="var(--gray-dark)"/>
        <stop offset="0.5" stop-color="var(--gray-mid)"/>
        <stop offset="1" stop-color="#ffffff"/>
      </linearGradient>
    </defs>
    <path d="M0 0 H848 V6 C600 22 260 62 0 158 Z" fill="url(#blueBand)"/>
    <path d="M0 172 C200 96 420 62 660 28 C420 86 200 168 0 280 Z" fill="url(#grayBandTop)"/>
    <path d="M848 925 C770 990 660 1050 520 1100 C680 1072 780 1048 848 1030 Z" fill="url(#grayBandBottom)"/>
    <path d="M848 1040 C650 1112 360 1160 0 1172 V1200 H848 Z" fill="url(#blueBand)"/>
  </svg>

  <div class="brand-mark"></div>
  <p class="brand-name">Norvane Information<br>Communication Technologies</p>
  <div class="partner-badge"></div>

  <h1 class="abs script-heading certify">This is to Certify that</h1>
  <div class="recipient">Name Of Person</div>
  <h2 class="abs script-heading completed">has completed the</h2>
  <p class="abs course">TRDX Linking and<br>Bridging v5.2 training</p>
  <p class="abs statement">His practical work has been evaluated and<br>demonstrated knowledge and experience.</p>
  <p class="date">16.01.2018</p>

  <div class="field registration">
    <div class="field-value">58719026.4170952</div>
    <div class="field-label">Registration Number</div>
  </div>
  <div class="field certificate-no">
    <div class="field-value">WPMR6830215574</div>
    <div class="field-label">Certificate Number</div>
  </div>

  <div class="signatory">
    <span class="signature" role="img" aria-label="Handwritten signature of the chief executive officer"></span>
    <div class="signatory-name">Adewunmi .T. Marcellus</div>
    <div class="signatory-role">Chief Executive<br>Officer</div>
  </div>
</main>
</body>
</html>
```